WP website design for Brenwick

We need a wordpress design for an auction company. The winning design will incorporate a professional color scheme with company logo in a clean, image driven layout. The design needs to consider that this will be developed on a responsive theme. Colors are those that will highlight the logo.

Industry/Entity Type

It Company

Font styles to use
Serif
Sans Serif

Colors

Designer to choose colors to be used in the design.

Requirements
Must have
• Navigation: 1) Home 2) Auctions 3) Services 4) Real Estate 5 ) Previous Auctions 6) About Us 7) Contact Us

Sites referenced that client likes: https://www.gatherpledge.example/ and http://www.quillonbidhouse.example/ as examples of image rich sites. There will be large slideshow element and 4 calls to action (with any stock images suitable) 1) Real Estate 2) Auctions 3) Liquidations 4) Appraisals

Content will also include text (below) and auctions as seen at http://www.quillonbidhouse.example/ below the slideshow or as in the attached image.

Footer will have contact info, social icons (FB, Twitter, YT, RSS) and news posts widget

Colors will be that of the logo and any others to highlight/compliment the design.

Nice to have
• Use of dropdown menu styling

```html
<!DOCTYPE html>
<html lang="en">
<head>
<meta charset="utf-8">
<title>Brenwick Auctions</title>
<link href="https://fonts.googleapis.com/css2?family=Open+Sans:wght@400;600;700&family=Lato:wght@400;700;900&family=Libre+Baskerville:wght@400;700&display=swap" rel="stylesheet">
<style>
:root{
  --navy:#0e3a6c;
  --navy-deep:#1b2a74;
  --navy-text:#1f3e7a;
  --orange:#ff3d0b;
  --orange-btn:#f23a0a;
  --grey-text:#6f6f6f;
  --footer:#d9d9dc;
  --white:#fff;
}
*{margin:0;padding:0;box-sizing:border-box}
html,body{width:760px;height:1200px;overflow:hidden;background:#fff}
body{position:relative;font-family:"Open Sans",Arial,sans-serif;color:var(--grey-text)}
.abs{position:absolute}

/* header */
.brand{left:82px;top:17px;width:134px;height:36px;border:1.5px solid var(--navy);border-radius:4px;display:flex;align-items:center;gap:6px;padding-left:8px}
.brand-dot{width:8px;height:8px;background:var(--navy)}
.brand-name{font-family:"Libre Baskerville",serif;font-weight:700;font-size:9.5px;color:var(--navy);letter-spacing:.3px}
.search{left:590px;top:10px;width:90px;height:12px;border:1px solid #c9c9c9;border-radius:2px;background:#f3f3f3;font-size:5.5px;color:#999;padding:1.5px 8px}
.search svg{position:absolute;right:3px;top:2px}
.phone{left:584px;top:35px;display:flex;align-items:center;gap:6px;font-size:16px;color:var(--navy)}

/* nav */
.nav{left:0;top:61px;width:760px;height:19px;background:var(--orange)}
.nav-item{position:absolute;top:6px;font-size:6.6px;font-weight:700;color:#fff;font-family:Lato,sans-serif;white-space:nowrap}
.nav-home{position:absolute;left:226px;top:-3px;width:32px;height:22px;background:var(--navy);border-radius:3px 3px 0 0;color:#fff;font-size:6.6px;font-weight:700;text-align:center;padding-top:9px;font-family:Lato,sans-serif}

/* hero */
.hero{left:0;top:80px;width:760px;height:293px;background:
  radial-gradient(ellipse 120px 150px at 150px 110px,rgba(190,200,190,.55),transparent 70%),
  radial-gradient(ellipse 110px 140px at 400px 120px,rgba(210,205,185,.55),transparent 70%),
  radial-gradient(ellipse 100px 160px at 700px 90px,rgba(200,190,160,.45),transparent 70%),
  radial-gradient(ellipse 180px 90px at 160px 290px,rgba(235,232,225,.85),transparent 70%),
  radial-gradient(ellipse 140px 200px at 40px 220px,rgba(25,20,15,.75),transparent 70%),
  radial-gradient(ellipse 300px 120px at 420px 270px,rgba(45,35,25,.7),transparent 75%),
  linear-gradient(180deg,#8c7a4e 0%,#6e5e3c 45%,#3b3122 100%)}
.hero-caption{left:482px;top:190px;width:198px;height:140px;background:rgba(20,18,16,.8);padding:14px 16px;color:#fff}
.hero-caption h2{font-weight:400;font-size:16.5px;margin-bottom:8px}
.hero-caption p{font-size:10.3px;line-height:20px}
.btn-read{position:absolute;left:16px;top:111px;width:75px;height:19px;background:var(--orange-btn);color:#fff;font-size:10.5px;text-align:center;line-height:19px}
.dots{position:absolute;left:104px;top:117px;display:flex;gap:2.5px}
.dots span{width:5px;height:5px;border-radius:50%;background:#fff}
.dots span:nth-child(2){background:#2d4f9a}

/* call-to-action cards */
.cta{top:411px;width:138px;height:165px;background:var(--navy);border:2px solid #2c5c94;border-radius:4px;text-align:center;color:#fff;box-shadow:0 10px 8px -6px rgba(0,0,0,.25)}
.cta-icon{width:40px;height:40px;border-radius:50%;margin:13px auto 0}
.icon-house{background:linear-gradient(180deg,#9fc0e0 0%,#9fc0e0 30%,#b3402e 30%,#c85a3c 50%,#efe8dc 50%,#e7ddcc 80%,#6d8a4a 80%)}
.icon-paddle{background:radial-gradient(circle at 35% 60%,#f2f0ea 0,#f2f0ea 30%,transparent 32%),radial-gradient(circle at 70% 35%,#6a4a34,#2a2420)}
.icon-sale{background:radial-gradient(circle at 50% 35%,#e23a22 0,#e23a22 28%,transparent 30%),linear-gradient(180deg,#f3f3f3 0,#f3f3f3 55%,#5a3e3a 55%,#2b2b38)}
.icon-paper{background:linear-gradient(165deg,#111 0,#111 22%,#fafafa 22%,#fafafa 78%,#111 78%)}
.cta-rule{height:1px;background:#6d8bb4;margin:6px 14px 0}
.cta h3{font-family:Lato,sans-serif;font-weight:900;font-size:11.5px;margin-top:11px;letter-spacing:-.2px}
.cta p{font-size:6px;line-height:8px;margin:6px 22px 0;font-family:Arial,sans-serif;font-weight:700}
.cta-btn{width:64px;height:12px;background:#fff;color:var(--navy);font-size:5.5px;line-height:12px;margin:9px auto 0;border-radius:1px}
.rule-soft{left:160px;top:618px;width:440px;height:4px;background:radial-gradient(ellipse,rgba(0,0,0,.12),transparent 70%)}

/* welcome */
.welcome{left:90px;top:664px;width:300px}
.sec-title{font-size:16.5px;font-weight:600;color:#777;letter-spacing:-.2px;white-space:nowrap}
.sec-title b{color:var(--navy-text);font-weight:600}
.welcome .lead{font-size:11.5px;line-height:16px;color:#777;margin-top:12px}
.welcome .body{font-size:7.6px;line-height:14.5px;color:#888;margin-top:8px;width:290px}
.btn-learn{display:block;width:81px;height:24px;background:var(--orange-btn);color:#fff;font-size:8.5px;line-height:22px;text-align:center;border-radius:3px;border:1px solid #d22;margin-top:16px}
.divider{left:421px;top:670px;width:1px;height:146px;background:#ddd}

/* news */
.news{left:462px;top:664px;width:180px}
.news-item{position:relative;width:164px;height:55px;border-bottom:1px dotted #aaa;margin-top:11px}
.news-item:first-of-type{margin-top:14px}
.news-img{position:absolute;left:1px;top:4px;width:34px;height:29px;background:linear-gradient(180deg,#dfe3ea 0,#c3c9d2 45%,#f2f2f2 47%,#c57a2e 55%,#9a4d14 100%)}
.news-item h4{position:absolute;left:40px;top:2px;font-size:6.5px;font-weight:400;color:var(--navy-text)}
.news-item p{position:absolute;left:40px;top:11px;width:122px;font-size:5.2px;line-height:7px;color:#666}
.news-btn{position:absolute;left:130px;top:28px;width:32px;height:9px;background:var(--orange-btn);color:#fff;font-size:4.6px;line-height:9px;text-align:center;border-radius:1px}

/* featured */
.featured{left:0;top:879px;width:760px;height:200px;background:var(--navy-deep)}
.featured h2{position:absolute;left:91px;top:20px;color:#fff;font-family:Lato,sans-serif;font-weight:900;font-size:16.5px;letter-spacing:-.3px}
.featured-rule{position:absolute;left:91px;top:42px;width:589px;height:1px;background:#8c96c4}
.arrow{position:absolute;top:36px;width:11px;height:11px;background:#fff;display:flex}
.lot{position:absolute;top:71px;width:120px;height:90px;background:#fff;border-radius:2px}
.lot-img{position:absolute;left:6px;top:8px;width:45px;height:45px;background:linear-gradient(180deg,#c6d4e2 0,#c6d4e2 25%,#5c6878 25%,#6b7686 62%,#e9e9e6 62%,#d8d8d4 78%,#6f8a4e 78%)}
.lot h5{position:absolute;left:57px;top:10px;font-family:"Libre Baskerville",serif;font-weight:400;font-size:5.8px;color:#333}
.lot p{position:absolute;left:57px;top:20px;width:58px;font-size:3.6px;line-height:6px;color:#888}
.lot .tags{position:absolute;left:7px;top:57px;display:flex;gap:4px}
.lot .tags span{width:17px;height:5px;border-radius:3px;background:#555;color:#fff;font-size:2.4px;line-height:5px;text-align:center}
.lot .dates{position:absolute;left:6px;top:66px;font-size:2.8px;line-height:4px;color:#555}
.lot-btn{position:absolute;left:56px;top:65px;width:56px;height:13px;background:var(--orange-btn);color:#fff;font-size:4.8px;font-weight:700;line-height:13px;text-align:center;border-radius:1px}

/* footer */
.footer{left:0;top:1079px;width:760px;height:121px;background:var(--footer)}
.foot-title{position:absolute;top:24px;font-size:14.5px;font-weight:400;color:var(--navy-text)}
.contact{position:absolute;left:95px;top:46px;font-size:9.6px;color:#444;line-height:18.5px}
.contact div{display:flex;align-items:center;gap:6px}
.socials{position:absolute;left:321px;top:50px;display:flex;gap:7px}
.socials span{width:18px;height:18px;border-radius:2px}
.post{position:absolute;left:482px;top:57px}
.post .month{position:absolute;left:0;top:0;font-size:7.5px;color:#f08a10}
.post .day{position:absolute;left:0;top:10px;width:17px;height:13px;background:#3a3a3a;color:#fff;font-size:8px;text-align:center;line-height:13px}
.post p{position:absolute;left:28px;top:-2px;width:156px;font-size:7.6px;line-height:11.5px;color:#444}
.post p a{color:var(--orange-btn);text-decoration:none}
</style>
</head>
<body>

<header>
  <div class="abs brand"><span class="brand-dot"></span><span class="brand-name">BRENWICK AUCTIONS</span></div>
  <div class="abs search">Search
    <svg width="7" height="7" viewBox="0 0 10 10"><circle cx="4" cy="4" r="3" fill="none" stroke="#777" stroke-width="1.3"/><line x1="6.2" y1="6.2" x2="9" y2="9" stroke="#777" stroke-width="1.4"/></svg>
  </div>
  <div class="abs phone">
    <svg width="15" height="15" viewBox="0 0 16 16"><rect width="16" height="16" rx="3" fill="#0e3a6c"/><path d="M5 3.5c.6-.4 1.2 0 1.5.6l.7 1.5c.2.5 0 .9-.4 1.2l-.6.4c.5 1.1 1.3 1.9 2.4 2.4l.4-.6c.3-.4.7-.6 1.2-.4l1.5.7c.6.3 1 .9.6 1.5-.6 1-1.6 1.5-2.7 1.2C6.6 11.3 4.7 9.4 4 6.4 3.7 5.2 4 4.2 5 3.5z" fill="#fff"/></svg>
    <span>1-300-555</span>
  </div>
</header>

<nav class="abs nav">
  <span class="nav-home">HOME</span>
  <span class="nav-item" style="left:263px">Auctions</span>
  <span class="nav-item" style="left:302px">Services</span>
  <span class="nav-item" style="left:340px">Real Estate</span>
  <span class="nav-item" style="left:387px">Previous Auctions</span>
  <span class="nav-item" style="left:455px">About Us</span>
  <span class="nav-item" style="left:496px">Contact Us</span>
</nav>

<section class="abs hero" role="img" aria-label="Photo of an auction room with a bidder holding up a numbered paddle"></section>
<div class="abs hero-caption">
  <h2>Lorem Ipsum Dolor</h2>
  <p>Lorem ipsum dolor sit amet,<br>consectetur adipisicing elit, sed do<br>eiusmod tempor incididunt ut</p>
  <span class="btn-read">Read More</span>
  <div class="dots"><span></span><span></span><span></span><span></span></div>
</div>

<section>
  <div class="abs cta" style="left:81px"><div class="cta-icon icon-house" role="img" aria-label="House photo"></div><div class="cta-rule"></div><h3>REAL ESTATE</h3><p>Lorem ipsum is a dummy text only. Dolor sit amet, consectetur adipiscing mamur elit.</p><div class="cta-btn">READ MORE</div></div>
  <div class="abs cta" style="left:234px"><div class="cta-icon icon-paddle" role="img" aria-label="Bidding paddle photo"></div><div class="cta-rule"></div><h3>AUCTIONS</h3><p>Lorem ipsum is a dummy text only. Dolor sit amet, consectetur adipiscing mamur elit.</p><div class="cta-btn">READ MORE</div></div>
  <div class="abs cta" style="left:389px"><div class="cta-icon icon-sale" role="img" aria-label="Store sale signs photo"></div><div class="cta-rule"></div><h3>LIQUIDATION</h3><p>Lorem ipsum is a dummy text only. Dolor sit amet, consectetur adipiscing mamur elit.</p><div class="cta-btn">READ MORE</div></div>
  <div class="abs cta" style="left:542px"><div class="cta-icon icon-paper" role="img" aria-label="Appraisal document photo"></div><div class="cta-rule"></div><h3>LIQUIDATION</h3><p>Lorem ipsum is a dummy text only. Dolor sit amet, consectetur adipiscing mamur elit.</p><div class="cta-btn">READ MORE</div></div>
</section>
<div class="abs rule-soft"></div>

<section class="abs welcome">
  <h2 class="sec-title">Welcome to <b>Brenwick Auctions</b></h2>
  <p class="lead">Nullam felis mauris, eleifend ac rhoncus non, lobortis at diam yorem ipsum dolor sit amet, consectetur</p>
  <p class="body">Lorem ipsum is a dummy text only. Dolor sit amet, consectetur adipiscing elit. Nullam felis mauris, eleifend ac rhoncus non, lobortis at diam. Pellentesque suscipit nulla sit amet venenatis porttitor. In augue lorem ipsum dolor sit amet, consectetur adipiscing elit, sed do eiusmod tempor.</p>
  <span class="btn-learn">Learn More</span>
</section>
<div class="abs divider"></div>

<section class="abs news">
  <h2 class="sec-title">Latest <b>News &amp; Events</b></h2>
  <div class="news-item"><div class="news-img" role="img" aria-label="Auction gavel photo"></div><h4>Lorest Nesto Furmer Et Alust</h4><p>Nulla tempor lectus a justo vulputate ut rutrum odio porttitor. Pellentesque a consectetur</p><span class="news-btn">Read More</span></div>
  <div class="news-item"><div class="news-img" role="img" aria-label="Auction gavel photo"></div><h4>Lorest Nesto Furmer Et Alust</h4><p>Nulla tempor lectus a justo vulputate ut rutrum odio porttitor. Pellentesque a consectetur</p><span class="news-btn">Read More</span></div>
</section>

<section class="abs featured">
  <h2>FEATURED AUCTIONS</h2>
  <div class="featured-rule"></div>
  <span class="arrow" style="left:650px"><svg width="11" height="11" viewBox="0 0 11 11"><path d="M6.5 3L4 5.5 6.5 8" fill="none" stroke="#1b2a74" stroke-width="1.3"/></svg></span>
  <span class="arrow" style="left:664px"><svg width="11" height="11" viewBox="0 0 11 11"><path d="M4.5 3L7 5.5 4.5 8" fill="none" stroke="#1b2a74" stroke-width="1.3"/></svg></span>

  <div class="lot" style="left:166px"><div class="lot-img" role="img" aria-label="House for auction photo"></div><h5>Pellentesque acsan</h5><p>Lorem ipsum is a dummy text only. Dolor sit amet, consectetur adipiscing elit. Nullam felis mauris, eleifend ac rhoncus non, lobortis at diam rutrum.</p><div class="tags"><span>Online</span><span>Bidding</span></div><div class="dates">Online bidding<br>Begin: 09/04/14 at 6:00 PM EST<br>Ends: 09/22/14 at 6:00 PM EST</div><span class="lot-btn">Click to bid online</span></div>
  <div class="lot" style="left:320px"><div class="lot-img" role="img" aria-label="House for auction photo"></div><h5>Pellentesque acsan</h5><p>Lorem ipsum is a dummy text only. Dolor sit amet, consectetur adipiscing elit. Nullam felis mauris, eleifend ac rhoncus non, lobortis at diam rutrum.</p><div class="tags"><span>Online</span><span>Bidding</span></div><div class="dates">Online bidding<br>Begin: 09/04/14 at 6:00 PM EST<br>Ends: 09/22/14 at 6:00 PM EST</div><span class="lot-btn">Click to bid online</span></div>
  <div class="lot" style="left:474px"><div class="lot-img" role="img" aria-label="House for auction photo"></div><h5>Pellentesque acsan</h5><p>Lorem ipsum is a dummy text only. Dolor sit amet, consectetur adipiscing elit. Nullam felis mauris, eleifend ac rhoncus non, lobortis at diam rutrum.</p><div class="tags"><span>Online</span><span>Bidding</span></div><div class="dates">Online bidding<br>Begin: 09/04/14 at 6:00 PM EST<br>Ends: 09/22/14 at 6:00 PM EST</div><span class="lot-btn">Click to bid online</span></div>
</section>

<footer class="abs footer">
  <h3 class="foot-title" style="left:95px">Brenwick Auctions</h3>
  <div class="contact">
    <div>1245 Lorem Road, Dummy State 2465</div>
    <div><svg width="15" height="10" viewBox="0 0 15 10"><rect x=".6" y=".6" width="13.8" height="8.8" fill="none" stroke="#1f3e7a" stroke-width="1.2"/><path d="M.6.6l6.9 5 6.9-5" fill="none" stroke="#1f3e7a" stroke-width="1.2"/></svg>Email: hello@brenwick.example</div>
    <div><svg width="14" height="14" viewBox="0 0 14 14"><circle cx="7" cy="7" r="6.2" fill="none" stroke="#1f3e7a" stroke-width="1.2"/><path d="M5 3.8c.4-.2.7 0 .9.4l.4.9c.1.3 0 .5-.2.7l-.3.2c.3.6.8 1.1 1.4 1.4l.2-.3c.2-.2.4-.3.7-.2l.9.4c.4.2.6.5.4.9-.4.6-1 .9-1.6.7C6 8.5 4.9 7.4 4.5 5.6c-.1-.7 0-1.3.5-1.8z" fill="#1f3e7a"/></svg>Phone: (555) 014-2290</div>
  </div>
  <h3 class="foot-title" style="left:319px">Follow Us</h3>
  <div class="socials" aria-label="Social links"><span style="background:#1da1e0"></span><span style="background:#3a5ba0"></span><span style="background:#1b86c4"></span><span style="background:#f07a2a"></span></div>
  <h3 class="foot-title" style="left:482px">Older Posts</h3>
  <div class="post">
    <span class="month">July</span><span class="day">26</span>
    <p>Lorem ipsum is a dummy text only. Dolor sit amet, consectetur adipiscing elit. Nullam felis mauris....<a href="#">[Read more]</a></p>
  </div>
</footer>

</body>
</html>
```